Local Roofing/Construction company business needs new biz card design

We need a new business card design, current cards are from the start of this operation and generic at best. We are a local Construction Company (General Contractor) with a majority of our work originating from insurance claims-exterior finish work is the main focus (Roofs-Siding-Gutters etc). Heavily involved with homeowners and the low ball offers they receive from insurance company's after a insurable event takes place. I have attached some of our original logo file(s) below.

```html
<!DOCTYPE html>
<html lang="en">
<head>
<meta charset="utf-8">
<title>Ironcrest Construction – Business Card</title>
<link rel="stylesheet" href="https://fonts.googleapis.com/css2?family=Open+Sans:wght@400;600;700;800&display=swap">
<style>
  :root {
    --stage: #e9e7e3;
    --card-dark: #0d1d1f;
    --card-light: #ffffff;
    --green: #3fae5a;
    --ink: #1b1f20;
    --ink-soft: #3a3f40;
    --on-dark: #f2f4f3;
  }
  * { box-sizing: border-box; margin: 0; padding: 0; }
  html, body { width: 1200px; height: 900px; overflow: hidden; }
  body {
    background: var(--stage);
    font-family: "Open Sans", Arial, sans-serif;
    position: relative;
  }
  .card {
    position: absolute;
    left: 290px;
    width: 620px;
    height: 354px;
    border-radius: 26px;
    overflow: hidden;
    box-shadow: 0 10px 26px rgba(0,0,0,.18);
  }
  .card--back { top: 58px; background: var(--card-dark); color: var(--on-dark); }
  .card--front { top: 478px; background: var(--card-light); color: var(--ink); }

  .brand {
    position: absolute;
    display: flex;
    align-items: center;
    gap: 14px;
    font-weight: 800;
    letter-spacing: .5px;
    text-transform: uppercase;
  }
  .brand__mark { width: 24px; height: 24px; background: currentColor; flex: none; }
  .brand__name { line-height: 1.05; }
  .card--back .brand { left: 34px; top: 112px; width: 280px; font-size: 30px; color: var(--green); }
  .card--front .brand { left: 34px; top: 40px; font-size: 32px; color: var(--card-dark); }

  /* back side */
  .services { position: absolute; right: 34px; top: 30px; width: 250px; text-align: right; }
  .section-title {
    color: var(--green); font-weight: 700; font-size: 14px;
    text-transform: uppercase; letter-spacing: .5px; margin-bottom: 4px;
  }
  .services li {
    list-style: none; font-size: 14px; line-height: 21px;
    display: flex; justify-content: flex-end; align-items: center; gap: 6px;
  }
  .services li svg { width: 13px; height: 13px; }
  .connect { position: absolute; right: 34px; top: 170px; text-align: right; font-size: 14px; line-height: 21px; }
  .emergency {
    display: flex; justify-content: flex-end; align-items: center; gap: 8px;
    font-weight: 700; font-size: 19px; margin-top: 4px;
  }
  .emergency svg { width: 18px; height: 18px; }
  .tagline {
    position: absolute; left: 0; right: 34px; bottom: 26px; text-align: right;
    color: var(--green); font-weight: 700; font-size: 14px;
    text-transform: uppercase; letter-spacing: .3px;
  }

  /* front side */
  .person { position: absolute; right: 330px; top: 200px; text-align: right; }
  .person__role { font-size: 15px; color: var(--ink-soft); }
  .person__name { font-size: 17px; font-weight: 700; text-transform: uppercase; }
  .divider { position: absolute; left: 300px; top: 176px; width: 1.5px; height: 120px; background: var(--green); }
  .contacts { position: absolute; left: 316px; top: 176px; font-size: 14px; color: var(--ink-soft); }
  .contacts li { list-style: none; display: flex; gap: 8px; line-height: 22px; }
  .contacts svg { width: 14px; height: 14px; flex: none; margin-top: 4px; fill: var(--ink); }
</style>
</head>
<body>

<section class="card card--back" aria-label="Card back">
  <div class="brand"><span class="brand__mark"></span><span class="brand__name">Ironcrest Construction</span></div>

  <div class="services">
    <h3 class="section-title">Our Services</h3>
    <ul>
      <li>Residential Roofing <svg viewBox="0 0 16 16"><path d="M2 8l4 4 8-9" fill="none" stroke="#3fae5a" stroke-width="2.4"/></svg></li>
      <li>Commercial Roofing <svg viewBox="0 0 16 16"><path d="M2 8l4 4 8-9" fill="none" stroke="#3fae5a" stroke-width="2.4"/></svg></li>
      <li>Storm Restoration <svg viewBox="0 0 16 16"><path d="M2 8l4 4 8-9" fill="none" stroke="#3fae5a" stroke-width="2.4"/></svg></li>
      <li>Exterior Finishes <svg viewBox="0 0 16 16"><path d="M2 8l4 4 8-9" fill="none" stroke="#3fae5a" stroke-width="2.4"/></svg></li>
    </ul>
  </div>

  <div class="connect">
    <h3 class="section-title">Connect</h3>
    <p>Monday - Friday: 8am - 6pm</p>
    <p>Saturday - Sunday: By Appointment Only</p>
    <p class="emergency">
      <svg viewBox="0 0 24 24"><path fill="#3fae5a" d="M6.6 10.8a15 15 0 0 0 6.6 6.6l2.2-2.2a1 1 0 0 1 1-.25 11.4 11.4 0 0 0 3.6.57 1 1 0 0 1 1 1V20a1 1 0 0 1-1 1A17 17 0 0 1 3 4a1 1 0 0 1 1-1h3.5a1 1 0 0 1 1 1c0 1.25.2 2.45.57 3.6a1 1 0 0 1-.25 1z"/></svg>
      Emergency: 555-014-7503
    </p>
  </div>

  <p class="tagline">You can trust our 30 years of combined experience</p>
</section>

<section class="card card--front" aria-label="Card front">
  <div class="brand"><span class="brand__mark"></span><span class="brand__name">Ironcrest Construction</span></div>

  <div class="person">
    <p class="person__role">Director</p>
    <p class="person__name">Daniel Reyes</p>
  </div>

  <div class="divider"></div>

  <ul class="contacts">
    <li><svg viewBox="0 0 24 24"><path d="M6.6 10.8a15 15 0 0 0 6.6 6.6l2.2-2.2a1 1 0 0 1 1-.25 11.4 11.4 0 0 0 3.6.57 1 1 0 0 1 1 1V20a1 1 0 0 1-1 1A17 17 0 0 1 3 4a1 1 0 0 1 1-1h3.5a1 1 0 0 1 1 1c0 1.25.2 2.45.57 3.6a1 1 0 0 1-.25 1z"/></svg>555-014-1014</li>
    <li><svg viewBox="0 0 24 24"><path d="M2 5h20v14H2z M2 5l10 8 10-8" fill="none" stroke="#1b1f20" stroke-width="2"/></svg>hello@ironcrestbuild.com</li>
    <li><svg viewBox="0 0 24 24"><g fill="none" stroke="#1b1f20" stroke-width="1.8"><circle cx="12" cy="12" r="10"/><ellipse cx="12" cy="12" rx="4.5" ry="10"/><path d="M2 12h20M4 7h16M4 17h16"/></g></svg>www.ironcrestbuild.com</li>
    <li><svg viewBox="0 0 24 24"><path d="M12 2a7 7 0 0 0-7 7c0 5 7 13 7 13s7-8 7-13a7 7 0 0 0-7-7zm0 9.5A2.5 2.5 0 1 1 12 6.5a2.5 2.5 0 0 1 0 5z"/></svg><span>48 Harlow Ridge Rd<br>Fairbrook, MO 63010</span></li>
  </ul>
</section>

</body>
</html>
```